Aged Care Consultancy Business needs a business card design

I need a two sided business card - I want it clean and professional. Surprise me

Target Market(s)

middle aged and ageing victorians

Industry/Entity Type

Health Care

Contact Information for Business Card

Text to be included

Logo
Aged Care Consulting Services
Professional, Reliable, Affordable

Tovan Brelsick
Director
0427 31 64 92 (larger)
1300 73 29 41
tovan@wadolire.com.au
www.wadolcare.com.au
Facebook (details TBA)

include little icons beside the contact info:

- Envelope = email
- Phone = phone
- Globe = website

Font styles to use
Serif
Sans Serif

Requirements
Must have
• look proffesional and clean

```html
<!DOCTYPE html>
<html lang="en">
<head>
<meta charset="utf-8">
<title>wadol care – Business Card</title>
<link rel="stylesheet" href="https://fonts.googleapis.com/css2?family=Source+Sans+3:wght@400;600;700&display=swap">
<style>
  :root {
    --backdrop: #dcd9d6;
    --card-face: #f4f2f0;
    --navy: #0b4283;
    --amber: #e8920a;
    --white: #ffffff;
    --faint-mark: #b9bcc4;
  }
  * { margin: 0; padding: 0; box-sizing: border-box; }
  html, body { width: 1200px; height: 900px; overflow: hidden; }
  body {
    position: relative;
    background: var(--backdrop);
    font-family: "Source Sans 3", "Helvetica Neue", Arial, sans-serif;
  }
  .card {
    position: absolute;
    background: var(--card-face);
    overflow: hidden;
    box-shadow: 0 6px 22px rgba(0,0,0,0.12);
  }
  .card--front { left: 237px; top: 61px; width: 556px; height: 344px; }
  .card--back  { left: 459px; top: 518px; width: 560px; height: 343px; }

  .brand-name {
    position: absolute;
    left: 0; right: 0;
    text-align: center;
    font-weight: 700;
    letter-spacing: 0.5px;
    color: var(--navy);
  }
  .card--front .brand-name { top: 110px; font-size: 48px; }
  .card--back .brand-name  { top: 108px; font-size: 48px; color: var(--faint-mark); }

  .band { position: absolute; left: 0; right: 0; bottom: 0; }
  .card--front .band { top: 186px; background: var(--navy); }
  .card--back .band  { top: 187px; background: var(--amber); }

  .holder {
    position: absolute;
    right: 295px; top: 43px;
    text-align: right;
    color: var(--white);
  }
  .holder-name  { font-size: 19.5px; font-weight: 600; line-height: 23px; }
  .holder-title { font-size: 15.5px; line-height: 18px; }
  .holder-phone { font-size: 17.5px; margin-top: 12px; line-height: 21px; }
  .holder-phone strong { font-weight: 600; }

  .contact-list {
    position: absolute;
    left: 282px; top: 42px;
    list-style: none;
    color: var(--white);
    font-size: 15.5px;
  }
  .contact-list li { display: flex; align-items: center; height: 20px; }
  .contact-list svg { width: 12px; height: 12px; margin-right: 10px; flex: none; }

  .tagline {
    position: absolute;
    left: 0; right: 0; top: 57px;
    text-align: center;
    color: var(--white);
    font-size: 16.5px;
    line-height: 20px;
  }
</style>
</head>
<body>
  <section class="card card--front">
    <div class="brand-name">wadol care</div>
    <div class="band">
      <div class="holder">
        <div class="holder-name">Tovan Brelsick</div>
        <div class="holder-title">Director</div>
        <div class="holder-phone"><strong>PHONE</strong> - 0427 31 64 92</div>
      </div>
      <ul class="contact-list">
        <li>
          <svg viewBox="0 0 12 12" aria-hidden="true"><path fill="#fff" d="M2.3 0.6l1.8 0.2 0.8 2.4-1.2 1c0.6 1.4 1.7 2.5 3.1 3.1l1-1.2 2.4 0.8 0.2 1.8c-0.1 0.8-0.7 1.3-1.5 1.3C4.5 10 1 6.6 1 2.1 1 1.3 1.5 0.7 2.3 0.6z"/></svg>
          1300 73 29 41
        </li>
        <li>
          <svg viewBox="0 0 12 12" aria-hidden="true"><rect x="1" y="2.5" width="10" height="7" fill="#fff"/><path d="M1 2.8l5 3.8 5-3.8" fill="none" stroke="#0b4283" stroke-width="1"/></svg>
          tovan@wadolire.com.au
        </li>
        <li>
          <svg viewBox="0 0 12 12" aria-hidden="true"><circle cx="6" cy="6" r="5" fill="none" stroke="#fff" stroke-width="1.2"/><ellipse cx="6" cy="6" rx="2" ry="5" fill="none" stroke="#fff" stroke-width="1"/><path d="M1 6h10" stroke="#fff" stroke-width="1"/></svg>
          www.wadolcare.com.au
        </li>
        <li>
          <svg viewBox="0 0 12 12" aria-hidden="true"><rect x="1" y="1" width="10" height="10" rx="1.5" fill="#fff"/></svg>
          linkbook.net/wadolcare
        </li>
      </ul>
    </div>
  </section>

  <section class="card card--back">
    <div class="brand-name">wadol care</div>
    <div class="band">
      <p class="tagline">Aged Care Consulting Services<br>Professional, Reliable, Affordable</p>
    </div>
  </section>
</body>
</html>
```